Quiet Lantern Sessions on Mental Health

I would like a website designed that would be used to upload podcasts, videos and written material about mental health. Where people will be being as honest, open and truthful as they can about mental health issues.
I would like it to look calming and soothing. Inspired by Vessaray's paintings and colour schemes.

I am on LinkedIn as Dr Helena Marwick - and twitter as drhelenamarwick

Target Market(s)

Healthcare professionals and users of services who want to think at a deeper level about the nature of mental illness

Number of Pages Required

1 page

```html
<!DOCTYPE html>
<html lang="en">
<head>
<meta charset="utf-8">
<title>Dr Helena Marwick</title>
<link href="https://fonts.googleapis.com/css2?family=Poppins:wght@400;500;600;700&family=Inter:ital,wght@0,400;0,500;1,400&display=swap" rel="stylesheet">
<style>
:root{
  --green:#4f7a68;
  --green-dark:#3f6656;
  --olive:#bcc08a;
  --ink:#1b1b1b;
  --text:#333;
  --mist:#edf0ee;
  --white:#fff;
  --star:#f39a1c;
}
*{box-sizing:border-box;margin:0;padding:0}
html,body{width:1200px;height:3983px;overflow:hidden}
body{position:relative;background:var(--white);font-family:"Inter",sans-serif;color:var(--text)}
.abs{position:absolute}
h1,h2,h3,.brand{font-family:"Poppins",sans-serif}
.accent{color:var(--green)}
.btn{position:absolute;display:flex;align-items:center;justify-content:center;font-family:"Poppins",sans-serif;font-weight:600;font-size:15px;color:var(--white);background:var(--green);border-radius:2px}
.photo{position:absolute}

/* header */
.site-header{position:absolute;left:0;top:0;width:1200px;height:100px;background:var(--white)}
.brand{position:absolute;left:97px;top:34px;font-size:27px;font-weight:500;color:var(--ink)}
.topbar{position:absolute;left:373px;top:0;width:827px;height:50px;background:var(--green);border-bottom-left-radius:14px;color:var(--white);font-size:16px}
.topbar .item{position:absolute;top:12px;display:flex;align-items:center;gap:14px}
.icon-dot{width:28px;height:28px;border-radius:50%;background:var(--white);display:flex;align-items:center;justify-content:center}
.social{position:absolute;width:28px;height:28px;border-radius:50%;background:var(--white)}
.nav a{position:absolute;top:66px;font-size:15px;color:var(--ink);text-decoration:none}

/* hero */
.hero{position:absolute;left:0;top:100px;width:1200px;height:599px}
.hero h1{position:absolute;left:97px;top:148px;font-size:56px;line-height:66px;font-weight:700;color:var(--white);letter-spacing:.5px}
.hero p{position:absolute;left:97px;top:287px;width:520px;font-size:14.5px;line-height:31px;color:var(--white)}

/* about */
.section-title{font-size:33px;font-weight:700;color:var(--ink);line-height:40px}
.body-copy{font-size:14.5px;line-height:31px;color:var(--text)}

/* lists */
.ticks li{list-style:none;position:relative;padding-left:26px;font-size:14.5px;line-height:31px;margin-bottom:8px}
.ticks li svg{position:absolute;left:0;top:9px}

/* podcasts */
.card{position:absolute;top:2620px;width:318px;height:412px;background:var(--white);box-shadow:0 3px 12px rgba(0,0,0,.12);border-radius:4px;overflow:hidden}
.card .photo{left:0;top:0;width:318px;height:239px}
.card h3{position:absolute;left:16px;top:262px;font-family:"Inter",sans-serif;font-weight:500;font-size:15.5px;color:var(--ink)}
.card p{position:absolute;left:17px;top:294px;width:290px;font-size:12px;line-height:26px}
.player{position:absolute;left:18px;top:369px;width:285px;height:28px;display:flex;align-items:center;gap:8px;font-size:12px;color:#666}
.player .bar{flex:1;height:3px;background:#9a9a9a;border-radius:2px}

/* testimonial */
.quote-text{position:absolute;left:598px;top:218px;width:500px;font-size:15px;line-height:31px;font-style:italic;color:var(--text)}

/* footer */
.site-footer{position:absolute;left:0;top:3622px;width:1200px;height:361px;background:#000;color:var(--white)}
.site-footer .nav a{color:var(--white);top:146px}
.contact-box{position:absolute;left:110px;top:195px;width:978px;height:78px;border:1px solid #bbb;display:flex}
.contact-box div{flex:1;display:flex;align-items:center;justify-content:center;gap:14px;font-size:15px;border-right:1px solid #bbb}
.contact-box div:last-child{border-right:none}
</style>
</head>
<body>

<header class="site-header">
  <div class="brand"><span class="accent">Dr Helena</span> Marwick</div>
  <div class="topbar">
    <div class="item" style="left:88px">
      <span class="icon-dot"><svg width="14" height="14" viewBox="0 0 24 24"><path fill="#4f7a68" d="M6.6 10.8a15 15 0 0 0 6.6 6.6l2.2-2.2a1 1 0 0 1 1-.25 11.4 11.4 0 0 0 3.6.57 1 1 0 0 1 1 1V20a1 1 0 0 1-1 1A17 17 0 0 1 3 4a1 1 0 0 1 1-1h3.5a1 1 0 0 1 1 1c0 1.250.2 2.450.57 3.57a1 1 0 0 1-.25 1z"/></svg></span>
      +1555 0134 2278
    </div>
    <div class="item" style="left:340px">
      <span class="icon-dot"><svg width="14" height="12" viewBox="0 0 24 20"><path fill="#4f7a68" d="M2 2h20v16H2z"/><path d="M2 3l10 8 10-8" stroke="#fff" stroke-width="2" fill="none"/></svg></span>
      info@drhelenamarwick.in
    </div>
    <span class="social" style="left:642px;top:11px"></span>
    <span class="social" style="left:678px;top:11px"></span>
  </div>
  <nav class="nav">
    <a style="left:400px">Home</a>
    <a style="left:487px">About Us</a>
    <a style="left:601px">Upload Podcasts</a>
    <a style="left:776px">Videos</a>
    <a style="left:873px">Testimonials</a>
    <a style="left:1016px">Contact Us</a>
  </nav>
</header>

<section class="hero">
  <div class="photo" role="img" aria-label="Smiling grey-haired woman in a white top against a soft, dark garden backdrop" style="left:0;top:0;width:1200px;height:599px;background:linear-gradient(90deg,#1f2a22 0%,#2b3a2e 45%,#4a5244 70%,#c9c3b8 82%,#3a3f33 100%)"></div>
  <h1>Welcome To<br>Dr Helena Marwick</h1>
  <p>Consultant Psychiatrist, Lead of the Clinician Support Working Group on the Impact of Loss in Care, Co-Chair Patient Care Forum, Vice Chair Talking Therapies Panel, Psychoanalyst, Group Analyst</p>
  <div class="btn" style="left:97px;top:395px;width:143px;height:46px">Book a free call</div>
  <div class="btn" style="left:269px;top:395px;width:152px;height:46px;background:transparent;border:2px solid var(--olive)">Get Started</div>
</section>

<section class="about">
  <svg class="abs" style="left:60px;top:895px" width="90" height="220" viewBox="0 0 90 220"><path d="M70 10 A100 100 0 0 0 70 210" stroke="url(#arcg)" stroke-width="20" fill="none"/><defs><linearGradient id="arcg" x1="0" y1="0" x2="0" y2="1"><stop offset="0" stop-color="#bcc08a"/><stop offset="1" stop-color="#4f7a68"/></linearGradient></defs></svg>
  <div class="abs" style="left:133px;top:800px;width:460px;height:422px;border:2px solid var(--olive);border-radius:18px"></div>
  <div class="photo" role="img" aria-label="Portrait of a woman with auburn hair on a dark background" style="left:125px;top:793px;width:456px;height:418px;border-radius:16px;background:radial-gradient(circle at 50% 45%,#b07c66 0%,#6a3a2a 35%,#161210 75%)"></div>
  <h2 class="section-title abs" style="left:634px;top:781px"><span class="accent">About</span> Us</h2>
  <p class="body-copy abs" style="left:634px;top:826px;width:470px">Sed ut perspiciatis unde omnis iste natus error sit voluptatem accusantium doloremque laudantium, totam rem aperiam, eaque ipsa quae ab illo inventore veritatis et quasi architecto beatae vitae dicta sunt explicabo. Nemo enim ipsam voluptatem quia voluptas sit aspernatur aut odit aut fugit, sed quia consequuntur magni dolores eos qui ratione voluptatem sequi nesciunt.</p>
  <p class="body-copy abs" style="left:634px;top:1042px;width:470px">Neque porro quisquam est, qui dolorem ipsum quia dolor sit amet, consectetur, adipisci velit, sed quia non numquam eius modi tempora incidunt ut labore et dolore magnam aliquam quaerat voluptatem.</p>
  <div class="btn" style="left:634px;top:1180px;width:131px;height:46px">Book A Call</div>
</section>

<section class="video">
  <div class="abs" style="left:94px;top:1310px;width:1013px;height:511px;border:4px solid var(--olive);border-radius:28px;overflow:hidden">
    <div class="photo" role="img" aria-label="Therapist talking with a young girl on a grey sofa in a bright room with plants" style="left:0;top:0;width:100%;height:100%;background:linear-gradient(100deg,#c9cfd6 0%,#9fb0c4 35%,#b9c3cf 60%,#8ea3bd 100%)"></div>
  </div>
  <svg class="abs" style="left:579px;top:1544px" width="44" height="44" viewBox="0 0 44 44"><circle cx="22" cy="22" r="22" fill="#000"/><path d="M17 13l13 9-13 9z" fill="#fff"/></svg>
</section>

<section class="written abs" style="left:0;top:1911px;width:1200px;height:594px;background:var(--mist)">
  <h2 class="section-title abs" style="left:97px;top:67px"><span class="accent">Written Material</span> About<br>Mental Health</h2>
  <ul class="ticks abs" style="left:97px;top:160px;width:470px">
    <li><svg width="16" height="16" viewBox="0 0 16 16"><circle cx="8" cy="8" r="8" fill="#4f7a68"/><path d="M4.5 8.2l2.3 2.3 4.7-4.7" stroke="#fff" stroke-width="1.8" fill="none"/></svg>Lorem ipsum dolor sit amet, consectetur adipiscing elit, sed do eiusmod tempor incididunt ut labore et dolore magna aliqua.</li>
    <li><svg width="16" height="16" viewBox="0 0 16 16"><circle cx="8" cy="8" r="8" fill="#4f7a68"/><path d="M4.5 8.2l2.3 2.3 4.7-4.7" stroke="#fff" stroke-width="1.8" fill="none"/></svg>Ut enim ad minim veniam, quis nostrud exercitation ullamco laboris nisi ut aliquip ex ea commodo consequat.</li>
    <li><svg width="16" height="16" viewBox="0 0 16 16"><circle cx="8" cy="8" r="8" fill="#4f7a68"/><path d="M4.5 8.2l2.3 2.3 4.7-4.7" stroke="#fff" stroke-width="1.8" fill="none"/></svg>Ut enim ad minim veniam, quis nostrud exercitation ullamco laboris nisi ut aliquip ex ea commodo consequat.</li>
    <li><svg width="16" height="16" viewBox="0 0 16 16"><circle cx="8" cy="8" r="8" fill="#4f7a68"/><path d="M4.5 8.2l2.3 2.3 4.7-4.7" stroke="#fff" stroke-width="1.8" fill="none"/></svg>Ut enim ad minim veniam, quis nostrud exercitation ullamco laboris nisi ut aliquip ex ea commodo consequat.</li>
  </ul>
  <div class="btn" style="left:97px;top:450px;width:135px;height:49px">Learn More</div>
  <svg class="abs" style="left:985px;top:54px" width="165" height="165" viewBox="0 0 165 165"><path d="M10 50 A72 72 0 1 1 110 155" stroke="url(#arcw)" stroke-width="14" fill="none"/><defs><linearGradient id="arcw" x1="0" y1="0" x2="1" y2="1"><stop offset="0" stop-color="#a9b683"/><stop offset="1" stop-color="#4f7a68"/></linearGradient></defs></svg>
  <div class="abs" style="left:588px;top:100px;width:512px;height:408px;border-radius:26px;border-left:12px solid var(--green);border-bottom:12px solid var(--green)"></div>
  <div class="photo" role="img" aria-label="Smiling bearded man in a therapy session while a counsellor takes notes on a clipboard" style="left:600px;top:100px;width:502px;height:405px;border-radius:20px;background:linear-gradient(110deg,#8b7a62 0%,#d9d6cf 40%,#a9b7c9 75%,#6f8fb8 100%)"></div>
</section>

<section class="podcasts">
  <h2 class="section-title abs" style="left:0;top:2558px;width:1200px;text-align:center"><span class="accent">Upload</span> Podcasts</h2>
  <svg class="abs" style="left:52px;top:2733px" width="24" height="24" viewBox="0 0 24 24"><circle cx="12" cy="12" r="11" stroke="#888" stroke-width="1.4" fill="none"/><path d="M16 12H8M11 8.5L7.5 12 11 15.5" stroke="#888" stroke-width="1.4" fill="none"/></svg>
  <svg class="abs" style="left:1128px;top:2733px" width="24" height="24" viewBox="0 0 24 24"><circle cx="12" cy="12" r="11" stroke="#222" stroke-width="1.4" fill="none"/><path d="M8 12h8M13 8.5l3.5 3.5-3.5 3.5" stroke="#222" stroke-width="1.4" fill="none"/></svg>

  <article class="card" style="left:97px">
    <div class="photo" role="img" aria-label="Laughing couple sitting together indoors" style="background:linear-gradient(120deg,#5b4a3a,#b08663 55%,#e7d4bd)"></div>
    <h3>Lorem ipsum dolor sit amet</h3>
    <p>Sed ut perspiciatis unde omnis iste natus error sit voluptatem accusantium doloremque</p>
    <div class="player"><svg width="26" height="26" viewBox="0 0 26 26"><circle cx="13" cy="13" r="13" fill="#9aa68a"/><path d="M10 8l8 5-8 5z" fill="#fff"/></svg>20:18<span class="bar"></span>30:18<svg width="16" height="14" viewBox="0 0 16 14"><path d="M1 5h3l4-4v12L4 9H1z" fill="#222"/><path d="M10.5 4.5a3.5 3.5 0 0 1 0 5M12.5 2.5a6.5 6.5 0 0 1 0 9" stroke="#222" stroke-width="1.4" fill="none"/></svg><svg width="15" height="15" viewBox="0 0 15 15"><path d="M7.5 1v8M4 6l3.5 3.5L11 6M1.5 13.5h12" stroke="#222" stroke-width="2" fill="none"/></svg></div>
  </article>
  <article class="card" style="left:441px">
    <div class="photo" role="img" aria-label="Man waving at a video call on a laptop" style="background:linear-gradient(120deg,#e9e6e1,#c8b8a4 50%,#f1efec)"></div>
    <h3>Lorem ipsum dolor sit amet</h3>
    <p>Sed ut perspiciatis unde omnis iste natus error sit voluptatem accusantium doloremque</p>
    <div class="player"><svg width="26" height="26" viewBox="0 0 26 26"><circle cx="13" cy="13" r="13" fill="#9aa68a"/><path d="M10 8l8 5-8 5z" fill="#fff"/></svg>20:18<span class="bar"></span>30:18<svg width="16" height="14" viewBox="0 0 16 14"><path d="M1 5h3l4-4v12L4 9H1z" fill="#222"/><path d="M10.5 4.5a3.5 3.5 0 0 1 0 5M12.5 2.5a6.5 6.5 0 0 1 0 9" stroke="#222" stroke-width="1.4" fill="none"/></svg><svg width="15" height="15" viewBox="0 0 15 15"><path d="M7.5 1v8M4 6l3.5 3.5L11 6M1.5 13.5h12" stroke="#222" stroke-width="2" fill="none"/></svg></div>
  </article>
  <article class="card" style="left:784px">
    <div class="photo" role="img" aria-label="Counsellor with a young girl on a sofa in a light room" style="background:linear-gradient(120deg,#f2f1ee,#c9cdd3 55%,#7d828c)"></div>
    <h3>Lorem ipsum dolor sit amet</h3>
    <p>Sed ut perspiciatis unde omnis iste natus error sit voluptatem accusantium doloremque</p>
    <div class="player"><svg width="26" height="26" viewBox="0 0 26 26"><circle cx="13" cy="13" r="13" fill="#9aa68a"/><path d="M10 8l8 5-8 5z" fill="#fff"/></svg>20:18<span class="bar"></span>30:18<svg width="16" height="14" viewBox="0 0 16 14"><path d="M1 5h3l4-4v12L4 9H1z" fill="#222"/><path d="M10.5 4.5a3.5 3.5 0 0 1 0 5M12.5 2.5a6.5 6.5 0 0 1 0 9" stroke="#222" stroke-width="1.4" fill="none"/></svg><svg width="15" height="15" viewBox="0 0 15 15"><path d="M7.5 1v8M4 6l3.5 3.5L11 6M1.5 13.5h12" stroke="#222" stroke-width="2" fill="none"/></svg></div>
  </article>
</section>

<section class="stories abs" style="left:0;top:3066px;width:1200px;height:556px;background:var(--mist)">
  <h2 class="section-title abs" style="left:0;top:60px;width:1200px;text-align:center">Client Success Stories</h2>
  <svg class="abs" style="left:46px;top:287px" width="20" height="30" viewBox="0 0 20 30"><path d="M16 2L3 15l13 13" stroke="#222" stroke-width="2.4" fill="none"/></svg>
  <svg class="abs" style="left:1134px;top:287px" width="20" height="30" viewBox="0 0 20 30"><path d="M4 2l13 13L4 28" stroke="#222" stroke-width="2.4" fill="none"/></svg>
  <div class="abs" style="left:99px;top:106px;width:384px;height:384px;border-radius:50%;background:conic-gradient(from 200deg,#4f7a68,#bcc08a,#4f7a68)"></div>
  <div class="photo" role="img" aria-label="Portrait of a woman wearing glasses and a grey scarf" style="left:113px;top:120px;width:356px;height:356px;border-radius:50%;background:radial-gradient(circle at 50% 40%,#9a8478 0%,#4b5667 55%,#2a3240 100%)"></div>
  <svg class="abs" style="left:598px;top:167px" width="44" height="36" viewBox="0 0 44 36"><path d="M0 36V20C0 8 6 2 17 0v7c-6 2-8 6-8 11h8v18zM25 36V20c0-12 6-18 17-20v7c-6 2-8 6-8 11h8v18z" fill="#1b1b1b"/></svg>
  <p class="quote-text">Lorem ipsum dolor sit amet, consectetur adipiscing elit, sed do eiusmod tempor incididunt ut labore et dolore magna aliqua. Ut enim ad minim veniam, quis nostrud exercitation ullamco laboris nisi ut aliquip ex ea commodo consequat. Duis aute irure dolor in velit esse cillum dolore eu fugiat nulla pariatur.</p>
  <div class="abs" style="left:596px;top:377px;font-size:17px;color:var(--green)">- Owen Pellham</div>
  <div class="abs" style="left:598px;top:405px;font-size:14.5px;color:var(--text)">Company Chairman United State.</div>
  <div class="abs" style="left:598px;top:438px;font-size:18px;letter-spacing:4px;color:var(--star)">★★★★★</div>
</section>

<footer class="site-footer">
  <div class="brand" style="left:0;top:62px;width:1200px;text-align:center;font-size:32px;font-weight:600;color:var(--white)">Dr Helena Marwick</div>
  <nav class="nav">
    <a style="left:248px">Home</a>
    <a style="left:336px">About Us</a>
    <a style="left:450px">Upload Podcasts</a>
    <a style="left:625px">Videos</a>
    <a style="left:723px">Testimonials</a>
    <a style="left:865px">Contact Us</a>
  </nav>
  <div class="contact-box">
    <div><span class="icon-dot" style="background:var(--green);width:34px;height:34px"><svg width="15" height="15" viewBox="0 0 24 24"><path fill="#fff" d="M6.6 10.8a15 15 0 0 0 6.6 6.6l2.2-2.2a1 1 0 0 1 1-.25 11.4 11.4 0 0 0 3.6.57 1 1 0 0 1 1 1V20a1 1 0 0 1-1 1A17 17 0 0 1 3 4a1 1 0 0 1 1-1h3.5a1 1 0 0 1 1 1c0 1.250.2 2.450.57 3.57a1 1 0 0 1-.25 1z"/></svg></span>+1555 0134 2278</div>
    <div><span class="icon-dot" style="background:var(--green);width:34px;height:34px"><svg width="15" height="12" viewBox="0 0 24 20"><path fill="#fff" d="M2 2h20v16H2z"/><path d="M2 3l10 8 10-8" stroke="#4f7a68" stroke-width="2" fill="none"/></svg></span>info@drhelenamarwick.in</div>
    <div><span class="icon-dot" style="background:var(--green);width:34px;height:34px"><svg width="13" height="17" viewBox="0 0 12 16"><path fill="#fff" d="M6 0a6 6 0 0 0-6 6c0 4.5 6 10 6 10s6-5.5 6-10a6 6 0 0 0-6-6zm0 8.2A2.2 2.2 0 1 1 6 3.8a2.2 2.2 0 0 1 0 4.4z"/></svg></span>Dr Helena Marwick,United State.</div>
  </div>
  <div class="abs" style="left:99px;top:308px;font-size:14.5px">Copyrights@2023.Dr Helena Marwick.All Rights Reserved</div>
  <span class="social" style="left:1034px;top:304px"></span>
  <span class="social" style="left:1073px;top:304px"></span>
</footer>

</body>
</html>
```